Walk Through the Fog Rise up, push on and onto your strongest game

BRIEF FOR BOOK FRONT COVER

• It needs to be iconic
• It needs to be a ‘clean’ design
• Needs to be seen on a bookshelf in an airport from 50 feet away
• No stick like figures/cartoon style or cutesy design
• The book appeals to both male and female readers
• This is a cross over book and covers a couple of genres like Marcus Televan’s book The Engine of Routine or Odile Fenwick’s Leaping Boldly. So it is primarily about taking better care of yourself personally, professionally and will appeal to those in business.
• The idea that a personal enriching life feeds into an engaged performer on the job – they feed off each other leading to increased engagement, productivity and fulfillment
• The dance analogy means that you are not sitting on the sidelines of your life or business
• It is laced with inspiring real life case studies
• Positioning of the book: People facing adversity and still come through better than ever and better equipped to what comes next.
• Want a cover that would attract a Pinnacle 50 CEO to buy the book for his staff
• My name as the author should be across the bottom KESTA VOREHAM MBA MCC
Updates

Project Deadline Extended Reason: A big thank you for all the designers who submitted a cover design and I have been spoilt for choiceI need to finalize the copy on the book cover and hence the need for an extension of time.Thanks for your understanding.Kesta Added Sunday, September 18, 2016

Target Market(s)

Professionals in the age group 25 - 55

Industry/Entity Type

Airport

Contact Information for Business Card

basic information and a very clean look

Logo Text

probably book title more important that it can be seen clearly when the size is reduced to a small size e.g. if sponsoring an event

Number of Pages Required

5+ page

Font styles to use
Sans Serif

Colors
ec1f27
f37122
abd037

Requirements
Must have
• info already provided

```html
<!DOCTYPE html>
<html lang="en">
<head>
<meta charset="UTF-8">
<title>Walk Through the Fog — Book Cover</title>
<link rel="stylesheet" href="https://fonts.googleapis.com/css2?family=Oswald:wght@500;600&display=swap">
<style>
  :root {
    --page-bg: #eeeeee;
    --cover-white: #ffffff;
    --title-blue: #2f6cb8;
    --band-blue: #2f6cb8;
    --ink: #111111;
    --art-blue: #dfe8f5;
    --art-red: #f6dcdc;
  }
  html, body {
    margin: 0;
    padding: 0;
    width: 1200px;
    height: 1200px;
    overflow: hidden;
    background: var(--page-bg);
  }
  .canvas {
    position: relative;
    width: 1200px;
    height: 1200px;
    display: flex;
    align-items: center;
    justify-content: center;
  }
  .book-cover {
    position: relative;
    width: 762px;
    height: 1120px;
    background: var(--cover-white);
    font-family: "Oswald", "Arial Narrow", sans-serif;
    text-align: center;
    overflow: hidden;
  }
  .book-title {
    position: absolute;
    top: 70px;
    left: 40px;
    right: 40px;
    margin: 0;
    color: var(--title-blue);
    font-weight: 600;
    text-transform: uppercase;
    line-height: 1.05;
  }
  .book-title .line {
    display: block;
    white-space: nowrap;
  }
  .book-title .line-one {
    font-size: 96px;
  }
  .book-title .line-two {
    font-size: 168px;
  }
  .cover-art {
    position: absolute;
    top: 440px;
    left: 226px;
    width: 310px;
    height: 340px;
    border-radius: 50% 50% 45% 45% / 40% 40% 60% 60%;
    background: radial-gradient(ellipse at 50% 78%, var(--art-red) 0%, var(--art-blue) 45%, var(--cover-white) 78%);
  }
  .subtitle {
    position: absolute;
    top: 808px;
    left: 30px;
    right: 30px;
    margin: 0;
    color: var(--ink);
    font-weight: 500;
    font-size: 44px;
    line-height: 1.28;
    text-transform: uppercase;
  }
  .subtitle .line {
    display: block;
    white-space: nowrap;
  }
  .author-band {
    position: absolute;
    left: 0;
    right: 0;
    bottom: 0;
    height: 130px;
    background: var(--band-blue);
    display: flex;
    align-items: center;
    justify-content: center;
  }
  .author-name {
    margin: 0;
    color: var(--cover-white);
    font-weight: 500;
    font-size: 50px;
    letter-spacing: 0.12em;
    text-transform: uppercase;
    white-space: nowrap;
  }
</style>
</head>
<body>
  <main class="canvas">
    <article class="book-cover">
      <h1 class="book-title">
        <span class="line line-one">Walk Through</span>
        <span class="line line-two">The Fog</span>
      </h1>
      <div class="cover-art" role="img" aria-label="Illustration of a small figure holding a red umbrella in falling rain, stepping onto a blue and red target with a curved red arrow around it"></div>
      <p class="subtitle">
        <span class="line">Rise up, push on</span>
        <span class="line">and onto your strongest game</span>
      </p>
      <footer class="author-band">
        <p class="author-name">Kesta Voreham MBA MCC</p>
      </footer>
    </article>
  </main>
</body>
</html>
```